Letterhead for Conveyancing Company

Use existing logo to create a letterhead for a conveyancing company. Must be able to be used in Microsoft Word. Easy to read and professional.
Contact information to be at the bottom.
Brightwater Conveyancing Pty Ltd
ACN 621 984 736PO Box 535 Campbelltown SA 5074
Mobile - 0461 739 285
Web address - www.brightwaterconveyancing.com.au

Requirements
Must have
• Logo and contact details.
• Simple and professional.

```html
<!DOCTYPE html>
<html lang="en">
<head>
<meta charset="utf-8">
<title>Brightwater Conveyancing Letterhead</title>
<link rel="stylesheet" href="https://fonts.googleapis.com/css2?family=Didact+Gothic&family=Roboto:wght@400;500;700&family=Montserrat:wght@800&display=swap">
<style>
  :root {
    --brand-pink: #e3449a;
    --paper: #f4f4f4;
    --backdrop: #e6e6e6;
    --ink: #555555;
    --ink-soft: #666666;
    --white: #ffffff;
    --signature-blue: #2c5fb0;
  }
  * { box-sizing: border-box; margin: 0; padding: 0; }
  html, body {
    width: 1024px;
    height: 1200px;
    overflow: hidden;
    background: var(--backdrop);
  }
  .letterhead {
    position: absolute;
    left: 98px;
    top: 20px;
    width: 828px;
    height: 1160px;
    background: var(--paper);
    box-shadow: 0 4px 18px rgba(0,0,0,0.12);
  }
  .letterhead__header {
    position: absolute;
    left: 0; top: 0;
    width: 100%;
    height: 193px;
    background: var(--brand-pink);
    color: var(--white);
  }
  .brand {
    position: absolute;
    left: 57px;
    top: 62px;
    display: flex;
    align-items: center;
    gap: 12px;
  }
  .brand__square {
    width: 22px;
    height: 22px;
    background: var(--white);
  }
  .brand__name {
    font-family: "Montserrat", sans-serif;
    font-weight: 800;
    font-size: 38px;
    letter-spacing: -0.5px;
    color: var(--white);
  }
  .contact {
    position: absolute;
    left: 538px;
    top: 61px;
    font-family: "Roboto", sans-serif;
    font-size: 12.5px;
    line-height: 18px;
  }
  .contact__company { font-weight: 700; }
  .contact__lines { margin-bottom: 6px; }
  .contact__item {
    display: flex;
    align-items: center;
    gap: 6px;
  }
  .contact__item svg { width: 11px; height: 11px; fill: var(--white); }
  .letter {
    position: absolute;
    left: 78px;
    top: 312px;
    width: 672px;
    font-family: "Didact Gothic", sans-serif;
    color: var(--ink);
  }
  .letter__greeting {
    font-size: 20px;
    color: var(--ink);
    margin-bottom: 34px;
  }
  .letter__body p {
    font-size: 11.2px;
    line-height: 16.8px;
    text-align: justify;
    color: var(--ink-soft);
    margin-bottom: 17px;
  }
  .letter__closing {
    font-size: 11.2px;
    color: var(--ink-soft);
    margin-top: 30px;
  }
  .letter__signature {
    display: block;
    margin-top: 52px;
    width: 145px;
    height: 66px;
    background: linear-gradient(135deg, rgba(44,95,176,0.18), rgba(44,95,176,0.08));
    border-radius: 4px;
  }
</style>
</head>
<body>
  <article class="letterhead">
    <header class="letterhead__header">
      <div class="brand">
        <span class="brand__square"></span>
        <span class="brand__name">Brightwater</span>
      </div>
      <div class="contact">
        <div class="contact__lines">
          <div class="contact__company">Brightwater Conveyancing Pty Ltd</div>
          <div>PO Box 812 Glenhaven SA 5091</div>
          <div>ACN 738 215 409</div>
        </div>
        <div class="contact__item">
          <svg viewBox="0 0 24 24" aria-hidden="true"><path d="M6.6 10.8a15.1 15.1 0 0 0 6.6 6.6l2.2-2.2a1 1 0 0 1 1-.25 11.4 11.4 0 0 0 3.6.57 1 1 0 0 1 1 1V20a1 1 0 0 1-1 1A17 17 0 0 1 3 4a1 1 0 0 1 1-1h3.5a1 1 0 0 1 1 1c0 1.25.2 2.45.57 3.57a1 1 0 0 1-.25 1z"/></svg>
          <span>0461 739 285</span>
        </div>
        <div class="contact__item">
          <svg viewBox="0 0 24 24" aria-hidden="true"><circle cx="12" cy="12" r="10"/><path d="M2 12h20M12 2c3 3 3 17 0 20M12 2c-3 3-3 17 0 20" stroke="#e3449a" stroke-width="1.6" fill="none"/></svg>
          <span>www.brightwaterconveyancing.com.au</span>
        </div>
      </div>
    </header>

    <section class="letter">
      <p class="letter__greeting">Dear Mr. Hartley,</p>
      <div class="letter__body">
        <p>Lorem ipsum dolor sit amet, consectetur adipiscing elit. Donec orci purus, luctus vitae dignissim eu, iaculis sed purus. Vivamus faucibus, ipsum nec aliquet viverra, leo mauris condimentum ligula, sit amet sagittis enim ligula quis arcu. Nam egestas tortor id nisi porttitor mattis. In tortor ante, ultricies in suscipit a, tempus non massa. Vivamus et auctor mi. Fusce vel massa nulla. Phasellus nec eros mauris, et scelerisque orci.</p>
        <p>Donec malesuada orci vitae nulla accumsan porta a id massa. Quisque accumsan iaculis magna sit amet fringilla. Maecenas consequat, magna eget tincidunt semper, odio nibh rutrum mi, id feugiat ante nisi eu risus. Vestibulum nunc orci, rhoncus a placerat in, ultricies in mi. Cras mattis varius eros, vel fringilla nisi suscipit eget. Quisque scelerisque sagittis nulla at porttitor.</p>
        <p>Sed id augue vitae urna euismod commodo aliquet a quam. Pellentesque arcu velit, cursus et malesuada ut, consequat et diam. Nullam erat sem, rhoncus id ullamcorper vitae, rhoncus et arcu. In ultricies ultricies nulla, ut rutrum nisi iaculis at. Donec eu magna a metus ornare faucibus. Fusce aliquet faucibus ultricies. Morbi semper, est id tincidunt gravida, sem arcu adipiscing lacus, ac bibendum nulla leo eu purus. Quisque nec diam sed risus consectetur accumsan quis quis nibh. Vestibulum id purus lorem.</p>
        <p>It is a long established fact that a reader will be distracted by the readable content of a page when looking at its layout. The point of using Lorem Ipsum is that it has a more-or-less normal distribution of letters, as opposed to using 'Content here, content here', making it look like readable English. Many desktop publishing packages</p>
      </div>
      <p class="letter__closing">Sincerely,</p>
      <span class="letter__signature" role="img" aria-label="Handwritten signature of the sender"></span>
    </section>
  </article>
</body>
</html>
```